Brindle Gardenworks Business Card

An eye catching, yet simple business card that includes;

1. our logo
2. office phone - 5127730194
3. email - brindlegardenworks@mailnest.example
4. website - www.brindlegardenworks.example
5. instagram - @brindlegardenworksrvt

```html
<!DOCTYPE html>
<html lang="en">
<head>
<meta charset="utf-8">
<title>Brindle Gardenworks Business Card</title>
<link href="https://fonts.googleapis.com/css2?family=Poppins:ital,wght@0,400;0,500;0,700;1,800&display=swap" rel="stylesheet">
<style>
  :root {
    --page-bg: #d9d3cb;
    --card-black: #050505;
    --brown: #7a3f24;
    --brown-light: #a0634a;
    --frost-top: #eef2f6;
    --frost-mid: #dfe3ea;
    --frost-low: #e8d4d6;
    --logo-ink: #6e3c26;
    --text-light: #e4e0dc;
    --text-soft: #c9b6a8;
  }
  html, body {
    margin: 0;
    width: 1200px;
    height: 970px;
    overflow: hidden;
    background: var(--page-bg);
  }
  .business-card {
    position: absolute;
    left: 80px;
    top: 188px;
    width: 1040px;
    height: 594px;
    border-radius: 22px;
    overflow: hidden;
    box-shadow: 0 18px 40px rgba(0,0,0,0.25);
    font-family: "Poppins", sans-serif;
  }
  .card-shapes { position: absolute; inset: 0; }
  .brand-name {
    position: absolute;
    left: 40px;
    top: 246px;
    width: 400px;
    text-align: center;
    margin: 0;
    font-weight: 700;
    font-size: 40px;
    line-height: 1.15;
    color: var(--logo-ink);
  }
  .contact-block {
    position: absolute;
    left: 570px;
    top: 108px;
    width: 440px;
    color: var(--text-light);
    white-space: nowrap;
  }
  .person-name {
    margin: 0;
    font-weight: 800;
    font-style: italic;
    font-size: 29px;
    line-height: 1.1;
    color: var(--brown);
  }
  .person-role {
    margin: 0;
    font-size: 22px;
    line-height: 1.2;
  }
  .address {
    margin: 62px 0 0;
    font-style: normal;
    font-size: 21px;
    line-height: 30px;
  }
  .contact-list {
    list-style: none;
    margin: 26px 0 0;
    padding: 0;
    font-size: 19.5px;
    line-height: 30px;
  }
  .contact-list li { display: flex; align-items: center; gap: 10px; }
  .contact-icon { width: 24px; height: 24px; flex: none; }
  .website {
    margin: 20px 0 0;
    font-size: 19.5px;
    color: var(--text-soft);
  }
</style>
</head>
<body>
  <section class="business-card">
    <svg class="card-shapes" viewBox="0 0 1040 594" width="1040" height="594">
      <defs>
        <linearGradient id="frost" x1="0" y1="0" x2="0" y2="1">
          <stop offset="0" stop-color="var(--frost-top)"/>
          <stop offset="0.6" stop-color="var(--frost-mid)"/>
          <stop offset="1" stop-color="var(--frost-low)"/>
        </linearGradient>
      </defs>
      <rect class="frosted-panel" width="1040" height="594" fill="url(#frost)" role="img" aria-label="Frosted translucent card surface"/>
      <path class="dark-panel" d="M475,0 C565,120 590,380 378,594 L1040,594 L1040,0 Z" fill="var(--card-black)"/>
      <path class="accent-swoosh" d="M528,190 C548,340 480,480 318,594 L372,594 C540,450 560,310 528,190 Z" fill="var(--brown)"/>
    </svg>

    <h1 class="brand-name">Brindle<br>Gardenworks</h1>

    <div class="contact-block">
      <p class="person-name">Marlo Venner</p>
      <p class="person-role">Manager</p>
      <address class="address">3871 Calloway Ln<br>Riverton, NC, 28999<br>United States</address>
      <ul class="contact-list">
        <li>
          <svg class="contact-icon" viewBox="0 0 26 26"><circle cx="13" cy="13" r="13" fill="var(--brown)"/><path d="M8 9c0-1 1-2 2-2h6c1 0 2 1 2 2v1h-3v-1h-4v1H8z M9 12h8l1 6H8z" fill="#fff"/></svg>
          <span>5127730194</span>
        </li>
        <li>
          <svg class="contact-icon" viewBox="0 0 26 26"><circle cx="13" cy="13" r="13" fill="var(--brown)"/><rect x="7" y="9" width="12" height="8" fill="none" stroke="#fff" stroke-width="1.5"/><path d="M7 9l6 5 6-5" fill="none" stroke="#fff" stroke-width="1.5"/></svg>
          <span>brindlegardenworks@mailnest.example</span>
        </li>
        <li>
          <svg class="contact-icon" viewBox="0 0 26 26"><circle cx="13" cy="13" r="13" fill="var(--brown)"/><circle cx="13" cy="13" r="3" fill="none" stroke="#fff" stroke-width="1.6"/><path d="M16 13v1.5a2 2 0 0 0 4 0V13a7 7 0 1 0-3 5.7" fill="none" stroke="#fff" stroke-width="1.6"/></svg>
          <span>@brindlegardenworksrvt</span>
        </li>
      </ul>
      <p class="website">www.brindlegardenworks.example</p>
    </div>
  </section>
</body>
</html>
```